We need a Chatterbox ad design for mobile app business.

"LUMAVO" app platform providing a range of services like home massage therapy or home hair cut needs 4 Chatterbox advertisement designs to hire the service providers. Each ad needs to bold one the professions and also show the others professions!! let say we we need one design emphasizing on Massage Therapist, one for hair stylists, one for tune up technicians, and that includes 4 professions : house keepers + lawn mowers, snow blowers and tutors. Each one of the designs requires a different content.
This app is gonna lunch in Thunder Bay/ON/Canada, So it is necessary to be mentioned. And even a design must be included the pandemic situation for some professions and EARNING A SIDE INCOME UP TO 50K PER YEAR AND ALSO TO BE YOUR OWN BOSS!.
Lumavo is service application that provides different ranges of services like automotive service, home cleaning, massage therapy and etc. So the design must be a very nice combination of services and very clear.

To get better understanding of the app please check it in the quindel market store or brisk store through following links:
https://apps.quindelmarket.example/details?id=com.lumavojobs

Requirements
Nice to have
• Apply green, silver and golden colors

```html
<!DOCTYPE html>
<html lang="en">
<head>
<meta charset="utf-8">
<title>Lumavo – Service Provider Ads</title>
<link rel="stylesheet" href="https://fonts.googleapis.com/css2?family=Oswald:wght@400;500;600;700&family=Roboto:wght@400;500;700&display=swap">
<style>
  :root {
    --page: #ffffff;
    --white: #ffffff;
    --gold: #c9a24a;
    --gold-light: #ecd493;
    --silver: #c7ccd1;
    --silver-dark: #8d949b;
    --massage-main: #c1621a;
    --massage-deep: #8a3f0c;
    --massage-photo-a: #d9b79a;
    --massage-photo-b: #6b4a37;
    --hair-main: #2f8a2c;
    --hair-deep: #1c5e1c;
    --hair-photo-a: #cfd8cf;
    --hair-photo-b: #4b4a42;
    --tune-main: #1f4fa0;
    --tune-deep: #0f2f6b;
    --tune-photo-a: #aebccd;
    --tune-photo-b: #2b3440;
  }
  * { box-sizing: border-box; margin: 0; padding: 0; }
  html, body { width: 747px; height: 1200px; overflow: hidden; background: var(--page); }
  body { position: relative; font-family: "Oswald", sans-serif; }

  .ad {
    position: absolute; left: 44px; width: 660px; height: 336px;
    background: var(--white); overflow: hidden;
    box-shadow: 8px 10px 18px rgba(0,0,0,.28);
  }
  .ad--massage { top: 40px; --main: var(--massage-main); --deep: var(--massage-deep); --pa: var(--massage-photo-a); --pb: var(--massage-photo-b); }
  .ad--hair    { top: 432px; --main: var(--hair-main); --deep: var(--hair-deep); --pa: var(--hair-photo-a); --pb: var(--hair-photo-b); }
  .ad--tune    { top: 824px; --main: var(--tune-main); --deep: var(--tune-deep); --pa: var(--tune-photo-a); --pb: var(--tune-photo-b); }

  .ad__stage { position: absolute; left: 0; top: 0; width: 660px; height: 284px; }
  .ad__photo {
    position: absolute; left: 30px; top: 22px; width: 600px; height: 262px;
    background: linear-gradient(110deg, var(--pa) 0%, var(--pb) 75%);
  }
  .ad__shapes { position: absolute; inset: 0; }

  .ad__copy {
    position: absolute; right: 40px; top: 28px; width: 270px; height: 252px;
    display: flex; flex-direction: column; align-items: flex-end;
    color: var(--white);
  }
  .ad--hair .ad__copy { top: 44px; }

  .ad__title {
    font-weight: 700; font-size: 42px; line-height: 1.02;
    text-align: right; letter-spacing: -.3px;
  }

  .pitch { width: 200px; margin-top: 8px; text-transform: uppercase; }
  .pitch__lead { font-size: 13.5px; font-weight: 500; letter-spacing: .3px; line-height: 1.3; }
  .pitch__amount { display: flex; align-items: center; gap: 3px; height: 40px; }
  .pitch__side {
    writing-mode: vertical-rl; transform: rotate(180deg);
    font-size: 8px; font-weight: 500; line-height: 1;
  }
  .pitch__side--right { transform: none; }
  .pitch__big { font-size: 38px; font-weight: 700; line-height: 1; }
  .pitch__tail { font-size: 10.5px; font-weight: 500; letter-spacing: .2px; line-height: 1.3; }

  .others { margin-top: 10px; text-transform: none; }
  .others__label { font-size: 12.5px; font-weight: 600; line-height: 1.3; }
  .others__list { font-family: "Roboto", sans-serif; font-size: 9.5px; line-height: 1.35; }

  .ad__footer {
    position: absolute; left: 0; bottom: 0; width: 660px; height: 52px;
    display: flex; align-items: center; gap: 22px; padding-left: 30px;
    background: var(--white);
  }
  .brand { display: flex; flex-direction: column; align-items: center; gap: 2px; }
  .brand__mark { width: 18px; height: 18px; border-radius: 50%; background: var(--main); }
  .brand__name { font-size: 10px; font-weight: 600; color: var(--main); letter-spacing: .8px; }
  .ad__getapp { font-family: "Roboto", sans-serif; font-size: 10px; color: var(--main); }
  .ad__getapp b { font-weight: 700; margin-right: 6px; }
</style>
</head>
<body>

<article class="ad ad--massage">
  <div class="ad__stage">
    <div class="ad__photo" role="img" aria-label="Photo of a therapist giving a relaxing back massage to a client on a massage table"></div>
    <svg class="ad__shapes" width="660" height="284" viewBox="0 0 660 284" aria-hidden="true">
      <polygon points="0,0 150,0 30,120 0,120" fill="var(--main)"/>
      <polygon points="0,0 60,0 0,60" fill="var(--deep)"/>
      <polygon points="340,22 630,22 630,284 300,284" fill="var(--main)" opacity=".92"/>
      <polygon points="560,0 660,0 660,90" fill="var(--silver)"/>
      <polygon points="600,0 660,0 660,40" fill="var(--gold)"/>
      <polygon points="560,284 660,200 660,284" fill="var(--gold-light)"/>
      <polygon points="600,284 660,236 660,284" fill="var(--gold)"/>
    </svg>
  </div>
  <div class="ad__copy">
    <h2 class="ad__title">Massage<br>therapist</h2>
    <div class="pitch">
      <p class="pitch__lead">Earning a side income</p>
      <p class="pitch__amount"><span class="pitch__side">Up to</span><span class="pitch__big">50K PER</span><span class="pitch__side pitch__side--right">Year</span></p>
      <p class="pitch__tail">And also to be your own boss!</p>
      <div class="others">
        <p class="others__label">Our other Services:</p>
        <p class="others__list">House keepers + Lawn mowers,<br>Snow blowers &amp; Tutors</p>
      </div>
    </div>
  </div>
  <footer class="ad__footer">
    <div class="brand"><span class="brand__mark"></span><span class="brand__name">LUMAVO</span></div>
    <p class="ad__getapp"><b>Get the APP :</b>apps.quindelmarket.example/details?id=com.lumavojobs</p>
  </footer>
</article>

<article class="ad ad--hair">
  <div class="ad__stage">
    <div class="ad__photo" role="img" aria-label="Photo of a hair stylist straightening a client's long dark hair in a salon"></div>
    <svg class="ad__shapes" width="660" height="284" viewBox="0 0 660 284" aria-hidden="true">
      <polygon points="0,0 200,0 60,140 0,140" fill="var(--main)"/>
      <polygon points="0,0 80,0 0,80" fill="var(--deep)"/>
      <polygon points="360,22 630,22 630,284 320,284" fill="var(--main)" opacity=".92"/>
      <polygon points="470,0 660,0 660,120 600,120" fill="var(--silver)" opacity=".7"/>
      <polygon points="560,284 660,190 660,284" fill="var(--silver)"/>
      <polygon points="610,284 660,238 660,284" fill="var(--silver-dark)"/>
    </svg>
  </div>
  <div class="ad__copy">
    <h2 class="ad__title">Hair Stylists</h2>
    <div class="pitch">
      <p class="pitch__lead">Earning a side income</p>
      <p class="pitch__amount"><span class="pitch__side">Up to</span><span class="pitch__big">50K PER</span><span class="pitch__side pitch__side--right">Year</span></p>
      <p class="pitch__tail">And also to be your own boss!</p>
      <div class="others">
        <p class="others__label">Our other Services:</p>
        <p class="others__list">House keepers + Lawn mowers,<br>Snow blowers &amp; Tutors</p>
      </div>
    </div>
  </div>
  <footer class="ad__footer">
    <div class="brand"><span class="brand__mark"></span><span class="brand__name">LUMAVO</span></div>
    <p class="ad__getapp"><b>Get the APP :</b>apps.quindelmarket.example/details?id=com.lumavojobs</p>
  </footer>
</article>

<article class="ad ad--tune">
  <div class="ad__stage">
    <div class="ad__photo" role="img" aria-label="Photo of a mechanic working under the open hood of a dark car in a garage"></div>
    <svg class="ad__shapes" width="660" height="284" viewBox="0 0 660 284" aria-hidden="true">
      <polygon points="0,0 170,0 40,130 0,130" fill="var(--main)"/>
      <polygon points="0,0 70,0 0,70" fill="var(--deep)"/>
      <polygon points="360,22 630,22 630,284 320,284" fill="var(--main)" opacity=".92"/>
      <polygon points="540,0 660,0 660,110" fill="var(--silver)"/>
      <polygon points="590,0 660,0 660,60" fill="var(--silver-dark)"/>
      <polygon points="540,284 660,170 660,284" fill="var(--deep)"/>
      <polygon points="600,284 660,226 660,284" fill="var(--silver)"/>
    </svg>
  </div>
  <div class="ad__copy">
    <h2 class="ad__title">Tune up<br>technicians</h2>
    <div class="pitch">
      <p class="pitch__lead">Earning a side income</p>
      <p class="pitch__amount"><span class="pitch__side">Up to</span><span class="pitch__big">50K PER</span><span class="pitch__side pitch__side--right">Year</span></p>
      <p class="pitch__tail">And also to be your own boss!</p>
      <div class="others">
        <p class="others__label">Our other Services:</p>
        <p class="others__list">House keepers + Lawn mowers,<br>Snow blowers &amp; Tutors</p>
      </div>
    </div>
  </div>
  <footer class="ad__footer">
    <div class="brand"><span class="brand__mark"></span><span class="brand__name">LUMAVO</span></div>
    <p class="ad__getapp"><b>Get the APP :</b>apps.quindelmarket.example/details?id=com.lumavojobs</p>
  </footer>
</article>

</body>
</html>
```